Stationery Design Project

I am a personal trainer in the fitness industry based in Miami. I have recently designed a logo for my company, now i need to market my name through selected stationery designs.
I need an email signature, invoice and a business card. I am looking for a design that is fresh and eye catching to my target audience.
Updates

Reason: Waiting for photo to be taken for business card.

Target Market(s)

25 to 65 years old - male and female - overweight, sedentary and athletic clientele - middle to wealthy economic class

Industry/Entity Type

Personal Trainer

Requirements
Must have
• Will attach Zip file with logo, template of invoice and personal information.
Will attach photo for business card in the next few days.
Nice to have
• Black backdrop logo image for banner of Invoice, with transparent images of my logo.
White backdrop logo image for Email signature, with font that works well with logo.

```html
<!DOCTYPE html>
<html lang="en">
<head>
<meta charset="utf-8">
<title>Brightpath Fitness Studio – Business Card</title>
<link rel="stylesheet" href="https://fonts.googleapis.com/css2?family=Open+Sans:wght@400;700&display=swap">
<style>
  :root {
    --backdrop: #ecebe8;
    --card: #ffffff;
    --ink: #3a3a3a;
    --ink-soft: #4d4d4d;
    --brand-orange: #e85d1f;
    --brand-yellow: #f7e13a;
    --brand-mid: #f39a24;
    --shadow: rgba(0, 0, 0, 0.28);
  }
  * { box-sizing: border-box; margin: 0; padding: 0; }
  html, body {
    width: 1200px;
    height: 403px;
    overflow: hidden;
    background: var(--backdrop);
    font-family: "Open Sans", Arial, sans-serif;
  }
  .stage { position: relative; width: 1200px; height: 403px; }
  .card {
    position: absolute;
    top: 48px;
    width: 535px;
    height: 304px;
    background: var(--card);
    box-shadow: 0 2px 5px var(--shadow);
    overflow: hidden;
  }
  .card--front { left: 51px; }
  .card--back { left: 626px; width: 531px; }

  .brand { position: absolute; display: flex; flex-direction: column; align-items: center; }
  .brand__dot {
    border-radius: 50%;
    background: var(--brand-mid);
  }
  .brand__name {
    color: var(--brand-orange);
    font-weight: 700;
    text-transform: uppercase;
    white-space: nowrap;
  }
  .card--front .brand { left: 30px; top: 26px; width: 260px; }
  .card--front .brand__dot { width: 84px; height: 84px; margin-bottom: 26px; }
  .card--front .brand__name { font-size: 19px; letter-spacing: 0.5px; line-height: 1.2; text-align: center; }

  .contact {
    position: absolute;
    left: 34px;
    top: 204px;
    list-style: none;
    color: var(--ink-soft);
    font-size: 13px;
    line-height: 23px;
  }

  .name-tab {
    position: absolute;
    right: 0;
    top: 206px;
    width: 201px;
    height: 62px;
    border-radius: 14px 0 0 14px;
    background: linear-gradient(90deg, var(--brand-yellow) 0%, var(--brand-mid) 45%, var(--brand-orange) 100%);
    color: #fff;
    text-align: center;
    padding-top: 10px;
    padding-left: 14px;
  }
  .name-tab__name { font-size: 16px; font-weight: 700; line-height: 20px; }
  .name-tab__role { font-size: 13px; line-height: 19px; }

  .card--back .brand { left: 0; right: 0; top: 46px; }
  .card--back .brand__dot { width: 140px; height: 140px; margin-bottom: 22px; }
  .card--back .brand__name { font-size: 20px; letter-spacing: 0.5px; }

  .web {
    position: absolute;
    left: 0;
    right: 0;
    top: 246px;
    text-align: center;
    color: var(--ink);
    font-size: 13px;
    letter-spacing: 1.3px;
  }
</style>
</head>
<body>
<main class="stage">
  <section class="card card--front" aria-label="Business card front">
    <div class="brand">
      <span class="brand__dot" aria-hidden="true"></span>
      <span class="brand__name">Brightpath Fitness Studio</span>
    </div>
    <ul class="contact">
      <li>P : 555-014-2290</li>
      <li>E : dana@brightpathfitness.com</li>
      <li>W : www.Brightpathfitness.com</li>
    </ul>
    <div class="name-tab">
      <p class="name-tab__name">Dana Morrow</p>
      <p class="name-tab__role">Personal Fitness Trainer</p>
    </div>
  </section>

  <section class="card card--back" aria-label="Business card back">
    <div class="brand">
      <span class="brand__dot" aria-hidden="true"></span>
      <span class="brand__name">Brightpath Fitness Studio</span>
    </div>
    <p class="web">www.Brightpathfitness.com</p>
  </section>
</main>
</body>
</html>
```